We need a website so we can post future events of our company about business motivation. The site have to include a calendar on the "Home" page that when the user cliks on the day of the event , there should open a small page with the information of the event (location,time,subject of the event...) . We need also an "About Us" page with information about our company and what we do as well as "Contact" page with our email and phone number and access to our facebook page. We would like to have a private access for users ("Restricted access") but they have to put their e-mail and password to access the special page (log in). On the 'special page' we would like to have some videos and photos that we will post on that page regularly .
Here is a website that would be an exemple of how we would like to have ours
http://northvalecapitalhub.example
The needs to be responsed and with backoffice

Industry/Entity Type

Business

Number of Pages Required

3 page

Colors
9bcb3c
f37122

Requirements
Must have
• Must have a restricted access page so the user can place a user name and a secret password.

```html
<!DOCTYPE html>
<html lang="en">
<head>
<meta charset="utf-8">
<title>Brightpath7go Events</title>
<link href="https://fonts.googleapis.com/css2?family=Exo+2:wght@300;400;500;700&display=swap" rel="stylesheet">
<style>
:root{
  --green:#8cc63f;
  --green-dark:#6fa82c;
  --orange:#f37122;
  --orange-dark:#c4501a;
  --black:#000;
  --panel:#121212;
  --panel-2:#1a1a1a;
  --text:#fff;
  --muted:#bdbdbd;
}
*{margin:0;padding:0;box-sizing:border-box}
html,body{width:837px;height:1200px;overflow:hidden;background:var(--black)}
body{font-family:"Exo 2",sans-serif;color:var(--text);position:relative}
.abs{position:absolute}
.accent{color:var(--orange)}

/* header */
.site-header{left:0;top:0;width:837px;height:68px;background:#0b0b0b}
.header-stripes{left:0;top:0}
.brand{left:118px;top:23px;width:154px;height:24px;background:#fff;color:#333;font-size:14px;letter-spacing:1px;display:flex;align-items:center;padding-left:6px;gap:6px}
.brand .mark{width:8px;height:8px;background:#555}
.auth{top:0;height:17px;background:var(--green);font-size:9px;display:flex;align-items:center;justify-content:center}
.nav{top:35px;display:flex;gap:17px;font-size:11px;left:438px}

/* hero */
.hero{left:0;top:68px;width:837px;height:320px;background:linear-gradient(180deg,#1a1620 0%,#4a2a3c 45%,#6b3b55 70%,#3a2633 100%)}
.hero-title{left:0;width:837px;top:146px;text-align:center;font-size:54px;font-weight:700;letter-spacing:-1px}
.hero-sub{left:304px;top:207px;width:241px;height:33px;background:rgba(255,255,255,.25);color:var(--orange);font-size:14px;font-weight:300;text-align:center;line-height:33px}
.arrow{top:203px;width:22px;height:22px;background:var(--orange)}
.cta{left:316px;top:285px;width:206px;height:39px;background:var(--orange);font-size:15px;text-align:center;line-height:39px}

/* search */
.search-bar{left:135px;top:370px;width:587px;height:62px;background:#111}
.field{top:392px;height:18px;background:#fff;color:#222;font-size:9px;padding-left:5px;line-height:18px}
.field::after{content:"";position:absolute;right:4px;top:7px;border:3px solid transparent;border-top:4px solid #222}
.search-btn{left:583px;top:380px;width:104px;height:30px;background:linear-gradient(var(--green),var(--green-dark));font-size:14px;font-weight:700;text-align:center;line-height:30px;letter-spacing:1px}

.section-title{font-size:16px;font-weight:400}

/* current events */
.events-panel{left:135px;top:470px;width:379px;height:125px;background:var(--panel)}
.thumb{border:2px solid #ddd}

/* upcoming */
.upcoming{left:535px;top:467px;width:170px;height:131px;background:var(--panel)}
.up-item{left:545px;display:flex;gap:12px}
.up-date{width:30px;text-align:center;font-size:24px;font-weight:500;line-height:22px}
.up-date small{display:block;font-size:9px;line-height:12px}
.up-info{border-left:1px solid #555;padding-left:8px;font-size:8px}
.up-info .venue{font-size:5px;color:var(--muted);margin-top:1px}
.ticket{display:inline-block;background:var(--orange);font-size:5px;padding:3px 5px;margin-top:5px}

/* blog */
.post-title{left:281px;top:662px;font-size:15px}
.post-meta{left:281px;top:686px;font-size:7px;color:var(--muted);display:flex;gap:22px}
.post-body{left:281px;top:703px;width:236px;font-size:6.6px;line-height:12px}
.read-more{left:281px;top:745px;width:44px;height:14px;background:var(--orange);font-size:6.5px;text-align:center;line-height:14px}

/* photos */
.photos-panel{left:137px;top:822px;width:563px;height:90px;background:#0d0d0d}

/* footer */
.site-footer{left:115px;top:940px;width:607px;height:260px;background:#0b0b0b}
.footer-brand{left:118px;top:1019px;width:117px;height:19px;background:#fff;color:#333;font-size:11px;letter-spacing:1px;padding-left:4px;line-height:19px}
.footer-about{left:118px;top:1056px;width:140px;font-size:7.6px;line-height:11.8px}
.recent{left:287px;display:flex;gap:8px}
.recent .t{width:38px;height:34px}
.recent p{font-size:6.8px;font-weight:700;line-height:12px;width:95px}
.recent span{display:block;font-weight:400;color:var(--muted);margin-top:3px}
.tweet{left:433px;width:130px;font-size:7px;line-height:11.5px}
.grid-photo{width:40px;height:40px}
.copyright{left:118px;top:1178px;font-size:7.5px}
.social{top:1175px;width:19px;height:19px;border:1.5px solid #fff;border-radius:50%}
</style>
</head>
<body>

<header class="site-header abs">
  <svg class="header-stripes abs" width="837" height="68">
    <polygon points="370,56 665,56 660,68 375,68" fill="var(--orange)"/>
    <polygon points="450,0 490,0 440,56 400,56" fill="#6b2f10"/>
    <polygon points="520,0 560,0 510,56 470,56" fill="#7a3512"/>
    <polygon points="580,56 598,56 588,68 570,68" fill="#0b0b0b"/>
  </svg>
  <div class="brand abs">Brightpath7go<span class="mark"></span></div>
  <div class="auth abs" style="left:647px;width:35px">Sign In</div>
  <div class="auth abs" style="left:684px;width:35px">Sign UP</div>
  <nav class="nav abs"><span>HOME</span><span>ABOUT US</span><span>EVENTS</span><span>TICKETS</span><span>CONTACT US</span></nav>
</header>

<section class="hero abs" role="img" aria-label="Crowd of people celebrating at a night event under colored lights"></section>
<h1 class="hero-title abs">EVENT NAME</h1>
<div class="hero-sub abs">Lorem ipsum dolor sit amet,</div>
<div class="arrow abs" style="left:138px"><svg width="22" height="22"><polyline points="14,5 8,11 14,17" fill="none" stroke="#fff" stroke-width="1.5"/></svg></div>
<div class="arrow abs" style="left:680px"><svg width="22" height="22"><polyline points="8,5 14,11 8,17" fill="none" stroke="#fff" stroke-width="1.5"/></svg></div>
<div class="cta abs">BOOK YOUR EVENT NOW</div>

<div class="search-bar abs">
  <svg class="abs" width="587" height="62"><polygon points="300,0 380,0 330,62 250,62" fill="#3a1e10"/><polygon points="400,0 440,0 390,62 350,62" fill="#2a160c"/></svg>
</div>
<div class="field abs" style="left:144px;width:115px">Select City</div>
<div class="field abs" style="left:278px;width:32px">15</div>
<div class="field abs" style="left:312px;width:36px">JUN</div>
<div class="field abs" style="left:350px;width:37px">2016</div>
<div class="search-btn abs">SEARCH</div>

<h2 class="section-title abs" style="left:132px;top:441px">CURRENT <span class="accent">EVENTS</span></h2>
<div class="events-panel abs"></div>
<div class="thumb abs" style="left:140px;top:475px;width:117px;height:115px;background:linear-gradient(#9ab0c8,#c9ccd0)" role="img" aria-label="Snowy street with a car"></div>
<div class="thumb abs" style="left:266px;top:475px;width:117px;height:115px;background:linear-gradient(#6e5a44,#8a4a3c)" role="img" aria-label="Children in costume"></div>
<div class="thumb abs" style="left:393px;top:475px;width:117px;height:115px;background:linear-gradient(#e8e8e8,#8a8a90)" role="img" aria-label="Group of business people"></div>

<h2 class="section-title abs" style="left:534px;top:443px">UPCOMMING <span class="accent">EVENTS</span></h2>
<div class="upcoming abs"></div>
<div class="up-item abs" style="top:485px"><div class="up-date">15<small>JUN</small></div><div class="up-info">DESPITE SECRET GUESTS<div class="venue">CLUB LUMENHALL</div><span class="ticket">BUY TICKET</span></div></div>
<div class="up-item abs" style="top:548px"><div class="up-date">20<small>JUN</small></div><div class="up-info">DESPITE SECRET GUESTS<div class="venue">CLUB LUMENHALL</div><span class="ticket">BUY TICKET</span></div></div>

<h2 class="section-title abs" style="left:132px;top:629px">LATEST FROM <span class="accent">THE BLOG</span></h2>
<div class="abs" style="left:143px;top:663px;width:122px;height:95px;background:linear-gradient(#2a1fd0,#3b1a6a 60%,#150d20)" role="img" aria-label="Performer on stage before a crowd"></div>
<div class="post-title abs">Sunrise Festival Organized in 2015</div>
<div class="post-meta abs"><span>admin</span><span>November 15th, 2015</span><span>6 comments</span></div>
<p class="post-body abs">Lorem ipsum dolor sit amet, consectetur adipisicing elit, sed do eiusmod tempor incididunt ut labore et dolore magna aliqua. Ut enim ad minim veniam, quis nostrud exercitation ullamco laboris nisi ut aliquip ex ea</p>
<div class="read-more abs">Read more</div>
<div class="abs" style="left:543px;top:662px;width:154px;height:96px;background:linear-gradient(#5aa0e0,#c8b060)" role="img" aria-label="Video of children at a playground"></div>
<svg class="abs" style="left:607px;top:699px" width="26" height="24"><rect width="26" height="24" fill="var(--orange)"/><polygon points="9,6 19,12 9,18" fill="#fff"/></svg>

<h2 class="section-title abs" style="left:137px;top:792px">LATEST <span class="accent">PHOTOS</span></h2>
<div class="photos-panel abs"></div>
<svg class="abs" style="left:340px;top:814px" width="300" height="100">
  <polygon points="10,0 60,0 55,9 5,9" fill="var(--orange-dark)"/>
  <polygon points="65,0 105,0 100,9 60,9" fill="#8a3a12"/>
  <polygon points="130,0 180,0 175,9 125,9" fill="var(--orange)"/>
  <polygon points="185,0 232,0 227,9 180,9" fill="var(--orange)"/>
  <polygon points="240,0 287,0 282,9 235,9" fill="var(--orange)"/>
  <rect x="150" y="96" width="80" height="3" fill="var(--orange)"/>
</svg>
<div class="abs" style="left:145px;top:829px;width:122px;height:75px;background:linear-gradient(#8cc4ee,#3d6fa0)" role="img" aria-label="Woman smiling against sky"></div>
<div class="abs" style="left:290px;top:829px;width:122px;height:75px;background:linear-gradient(#5a5a60,#b08070)" role="img" aria-label="Business people in a meeting"></div>
<div class="abs" style="left:432px;top:829px;width:122px;height:75px;background:linear-gradient(#d0ccc4,#5a4a3c)" role="img" aria-label="Colleagues working together"></div>
<div class="abs" style="left:571px;top:829px;width:122px;height:75px;background:linear-gradient(#e6e6e6,#3a3a44)" role="img" aria-label="Team giving thumbs up"></div>

<footer class="site-footer abs"></footer>
<div class="footer-brand abs">Brightpath7go</div>
<p class="footer-about abs">Lorem ipsum dolor sit amet, consectetur adipisicing elit, sed do eiusmod tempor incididunt ut labore et dolore magna aliqua. Ut enim ad minim veniam, quis nostrud exercitation ullamco laboris nisi ut aliquip ex ea commodo consequat.</p>

<h3 class="section-title abs" style="left:287px;top:1002px;font-size:13px">RECENT <span class="accent">POSTS</span></h3>
<div class="recent abs" style="top:1030px"><div class="t" style="background:linear-gradient(#8aa8c8,#4a5a70)" role="img" aria-label="Festival crowd"></div><p>Sunrise Festival organized China 2015<span>December 15, 2015</span></p></div>
<div class="recent abs" style="top:1074px"><div class="t" style="background:linear-gradient(#8aa8c8,#4a5a70)" role="img" aria-label="Festival crowd"></div><p>Thousands celebrities at Johnnie Night<span>December 15, 2015</span></p></div>
<div class="recent abs" style="top:1118px"><div class="t" style="background:linear-gradient(#8aa8c8,#4a5a70)" role="img" aria-label="Festival crowd"></div><p>Clubbing royalty Night Shift Turns 18<span>December 15, 2015</span></p></div>

<h3 class="section-title abs" style="left:432px;top:1002px;font-size:13px">TWITTER FEED</h3>
<p class="tweet abs" style="top:1030px">●<br>December 15, 2015<br>http://northvalecapitalhub.example</p>
<p class="tweet abs" style="top:1084px">● Lorem ipsum dolor sit amet, consectetur adipisicing elit, sed do eiusmod tempor incididunt ut labore et dolore magna aliqua. Ut enim ad 4 months ago</p>

<h3 class="section-title abs" style="left:583px;top:1002px;font-size:11px;font-weight:700">PHOTOS</h3>
<div class="grid-photo abs" style="left:580px;top:1030px;background:linear-gradient(#eee,#b44)" role="img" aria-label="Portrait photo"></div>
<div class="grid-photo abs" style="left:628px;top:1030px;background:linear-gradient(#a88,#433)" role="img" aria-label="Portrait photo"></div>
<div class="grid-photo abs" style="left:676px;top:1030px;background:linear-gradient(#c33,#622)" role="img" aria-label="Portrait photo"></div>
<div class="grid-photo abs" style="left:580px;top:1078px;background:linear-gradient(#48a,#a64)" role="img" aria-label="Portrait photo"></div>
<div class="grid-photo abs" style="left:628px;top:1078px;background:linear-gradient(#ccd,#557)" role="img" aria-label="Portrait photo"></div>
<div class="grid-photo abs" style="left:676px;top:1078px;background:linear-gradient(#aab,#446)" role="img" aria-label="Portrait photo"></div>
<div class="grid-photo abs" style="left:580px;top:1126px;background:linear-gradient(#8bd,#357)" role="img" aria-label="Portrait photo"></div>
<div class="grid-photo abs" style="left:628px;top:1126px;background:linear-gradient(#ddd,#888)" role="img" aria-label="Portrait photo"></div>
<div class="grid-photo abs" style="left:676px;top:1126px;background:linear-gradient(#eee,#999)" role="img" aria-label="Portrait photo"></div>

<p class="copyright abs">Copyright@2016brightpath7go.example-All rights reserve.</p>
<span class="social abs" style="left:616px"></span>
<span class="social abs" style="left:645px;border-color:var(--orange)"></span>
<span class="social abs" style="left:670px;border-color:var(--green)"></span>

</body>
</html>
```